Halvicek Law Group, PLLC
Business card and stationery
Professional
Marcus T. Halvicek, Esq.
President
248 Perrin Avenue
Suite 3407
New York, New York 10093
mhalvicek@halviceklawgroup.example
www.halviceklawgroup.example
Using Ivory-colored card stock
There are 2 additional staff members that need cards:
nothing

```html
<!DOCTYPE html>
<html lang="en">
<head>
<meta charset="utf-8">
<title>Halvicek Law Group, PLLC — Business Card</title>
<link href="https://fonts.googleapis.com/css2?family=Open+Sans:wght@400;600&display=swap" rel="stylesheet">
<style>
  :root {
    --backdrop: #e6e0d6;
    --card-maroon: #4a1116;
    --card-ivory: #fffdf7;
    --card-shadow-edge: #0d0d0d;
    --brand-maroon: #4a1116;
    --text-light: #ffffff;
  }
  html, body {
    margin: 0;
    padding: 0;
    width: 1200px;
    height: 778px;
    overflow: hidden;
    background: var(--backdrop);
    font-family: "Open Sans", Arial, sans-serif;
  }
  .business-card {
    position: absolute;
    left: 150px;
    top: 142px;
    width: 900px;
    height: 494px;
    border-radius: 32px;
    overflow: hidden;
    background: var(--card-maroon);
    box-shadow: 0 6px 18px rgba(0, 0, 0, 0.25);
  }
  .card-shapes {
    position: absolute;
    inset: 0;
  }
  .brand-name {
    position: absolute;
    left: 30px;
    top: 190px;
    width: 420px;
    margin: 0;
    text-align: center;
    color: var(--brand-maroon);
    font-weight: 600;
    font-size: 34px;
    line-height: 1.35;
    letter-spacing: 3px;
    text-transform: uppercase;
  }
  .contact-block {
    position: absolute;
    right: 30px;
    top: 0;
    width: 440px;
    color: var(--text-light);
    text-align: right;
  }
  .person-name {
    position: absolute;
    right: 0;
    top: 38px;
    margin: 0;
    font-size: 29px;
    font-weight: 600;
    white-space: nowrap;
  }
  .person-title {
    position: absolute;
    right: 0;
    top: 80px;
    margin: 0;
    font-size: 21px;
    font-weight: 600;
  }
  .address {
    position: absolute;
    right: 30px;
    top: 218px;
    margin: 0;
    font-style: normal;
    font-size: 20px;
    line-height: 38px;
    white-space: nowrap;
  }
  .contact-list {
    position: absolute;
    right: 0;
    top: 362px;
    margin: 0;
    padding: 0;
    list-style: none;
    font-size: 20px;
    line-height: 30px;
  }
  .contact-list li {
    display: flex;
    justify-content: flex-end;
    align-items: center;
    gap: 10px;
    white-space: nowrap;
  }
  .contact-icon {
    width: 18px;
    height: 18px;
    flex: none;
  }
</style>
</head>
<body>
  <section class="business-card" aria-label="Business card for Marcus T. Halvicek, Esq.">
    <svg class="card-shapes" width="900" height="494" viewBox="0 0 900 494" aria-hidden="true">
      <ellipse cx="8" cy="247" rx="520" ry="300" fill="var(--card-shadow-edge)"/>
      <ellipse cx="-20" cy="247" rx="520" ry="300" fill="var(--card-ivory)"/>
    </svg>

    <p class="brand-name">Halvicek Law Group, PLLC</p>

    <div class="contact-block">
      <h1 class="person-name">Marcus T. Halvicek, Esq.</h1>
      <p class="person-title">President</p>

      <address class="address">
        248 Perrin Avenue<br>
        Suite 3407<br>
        New York, New York 10093
      </address>

      <ul class="contact-list">
        <li>212-555-0148
          <svg class="contact-icon" viewBox="0 0 24 24" aria-label="phone"><path fill="#fff" d="M6.6 10.8a15 15 0 0 0 6.6 6.6l2.2-2.2c.3-.3.7-.4 1-.2 1.1.4 2.3.6 3.6.6.6 0 1 .4 1 1V20c0 .6-.4 1-1 1C10.6 21 3 13.4 3 4c0-.6.4-1 1-1h3.5c.6 0 1 .4 1 1 0 1.3.2 2.5.6 3.6.1.3 0 .7-.2 1z"/></svg>
        </li>
        <li>212-555-0193
          <svg class="contact-icon" viewBox="0 0 24 24" aria-label="fax"><path fill="#fff" d="M7 3h10v5H7zM4 9h16a1 1 0 0 1 1 1v9a1 1 0 0 1-1 1H4a1 1 0 0 1-1-1v-9a1 1 0 0 1 1-1zm3 4v2h10v-2z"/></svg>
        </li>
        <li>mhalvicek@halviceklawgroup.example
          <svg class="contact-icon" viewBox="0 0 24 24" aria-label="email"><path fill="#fff" d="M3 5h18v14H3zm2 2v.5l7 5 7-5V7z"/></svg>
        </li>
        <li>www.halviceklawgroup.example
          <svg class="contact-icon" viewBox="0 0 24 24" aria-label="website"><circle cx="12" cy="12" r="9" fill="none" stroke="#fff" stroke-width="2"/><path d="M3 12h18M12 3c3 3 3 15 0 18M12 3c-3 3-3 15 0 18" fill="none" stroke="#fff" stroke-width="1.6"/></svg>
        </li>
      </ul>
    </div>
  </section>
</body>
</html>
```